New Bicycle shop business card

Hi!
I'm looking for a business card for my new proffesional bike mechanics shop. This shop is only for fixing broken bikes and not selling bikes.
Peferbly a modern and sleek and modern design.
Colors: black, grey, red, white
Information:
Name: Velowerkplaats Martens
Shop owner: Bart Martens & Sofie Vanhulle
Website: www.velowerkplaats-martens.be
Email: info@velowerkplaats-martens.be
Phone number: +32471936208
Street adres: Molenweg 57
9470 Oostmolenbeek
Slogan/shop information: Herstellingen van alle merken.
Logo: see files.
Target Market(s)
People who seek a mechanic to fix or upgrade their bikes.
Contact Information for Business Card
Information:
Website: info@velowerkplaats-martens.be
9470 Oostmolenbeek
Logo: see files.

```html
<!DOCTYPE html>
<html lang="nl">
<head>
<meta charset="utf-8">
<title>Velowerkplaats Martens – business card</title>
<link href="https://fonts.googleapis.com/css2?family=Open+Sans:wght@400;600;700&display=swap" rel="stylesheet">
<style>
  :root {
    --red: #ec1f2d;
    --black: #141414;
    --grey: #3d4044;
    --white: #ffffff;
    --backdrop: #5a5d61;
  }
  * { box-sizing: border-box; margin: 0; padding: 0; }
  html, body { width: 1200px; height: 900px; overflow: hidden; }
  body {
    background: var(--backdrop);
    font-family: "Open Sans", Arial, sans-serif;
    position: relative;
  }
  .card {
    position: absolute;
    left: 250px;
    width: 700px;
    height: 400px;
    border-radius: 36px;
    overflow: hidden;
  }
  .card--front { top: 40px; background: var(--red); }
  .card--back { top: 460px; background: var(--white); color: var(--black); }

  .brand {
    position: absolute;
    display: flex;
    align-items: center;
    gap: 14px;
  }
  .brand__dot { border-radius: 50%; flex: none; }
  .brand__name { font-weight: 700; white-space: nowrap; }

  /* front */
  .card--front .brand { left: 0; right: 0; top: 160px; justify-content: center; }
  .card--front .brand__dot { width: 34px; height: 34px; background: var(--black); }
  .card--front .brand__name { font-size: 36px; color: var(--black); }

  .slogan-band {
    position: absolute;
    left: 0; right: 0;
    top: 262px;
    height: 52px;
    background: linear-gradient(90deg, rgba(20,20,20,0) 0%, rgba(20,20,20,0.95) 35%, rgba(20,20,20,0.95) 65%, rgba(20,20,20,0) 100%);
    display: flex;
    align-items: center;
    justify-content: center;
  }
  .slogan {
    color: var(--white);
    font-size: 16px;
    font-weight: 600;
    letter-spacing: 0.3px;
  }

  /* back */
  .card--back .brand { right: 40px; top: 60px; }
  .card--back .brand__dot { width: 22px; height: 22px; background: var(--red); }
  .card--back .brand__name { font-size: 24px; color: var(--black); }

  .owners {
    position: absolute;
    left: 60px;
    top: 128px;
    width: 340px;
    text-align: center;
  }
  .owners__label { font-size: 22px; font-weight: 600; }
  .owners__names { font-size: 22px; font-weight: 600; color: var(--red); line-height: 1.25; }
  .owners__rule { display: block; height: 3px; background: var(--black); width: 250px; margin: 14px 0 0 40px; }

  .company {
    position: absolute;
    left: 70px;
    top: 240px;
    padding-left: 16px;
    border-left: 4px solid var(--red);
  }
  .company__name { font-size: 22px; font-weight: 600; line-height: 1.25; }
  .company__name-accent { color: var(--red); }
  .company__role { font-size: 16px; font-weight: 600; }

  .contacts {
    position: absolute;
    left: 90px;
    top: 312px;
    list-style: none;
    font-size: 14px;
    color: var(--grey);
  }
  .contacts__item { display: flex; align-items: center; gap: 10px; line-height: 22px; }
  .contacts__icon { width: 13px; height: 13px; fill: var(--red); flex: none; }

  .address {
    position: absolute;
    right: 40px;
    top: 220px;
    font-size: 15px;
    font-style: normal;
    color: var(--grey);
    line-height: 1.35;
    text-align: left;
  }
</style>
</head>
<body>

<section class="card card--front" aria-label="Card front">
  <div class="brand">
    <span class="brand__dot"></span>
    <span class="brand__name">Velowerkplaats Martens</span>
  </div>
  <div class="slogan-band">
    <p class="slogan">Herstellingen van alle merken.</p>
  </div>
</section>

<section class="card card--back" aria-label="Card back">
  <div class="brand">
    <span class="brand__dot"></span>
    <span class="brand__name">Velowerkplaats Martens</span>
  </div>

  <div class="owners">
    <p class="owners__label">Shop owner:</p>
    <p class="owners__names">Bart Martens &amp; Sofie Vanhulle</p>
    <span class="owners__rule"></span>
  </div>

  <div class="company">
    <p class="company__name"><span class="company__name-accent">Velowerkplaats</span> Martens</p>
    <p class="company__role">General Manager</p>
  </div>

  <ul class="contacts">
    <li class="contacts__item">
      <svg class="contacts__icon" viewBox="0 0 24 24" aria-hidden="true"><path d="M6.6 10.8a15 15 0 0 0 6.6 6.6l2.2-2.2a1 1 0 0 1 1-.25 11.4 11.4 0 0 0 3.6.57 1 1 0 0 1 1 1V20a1 1 0 0 1-1 1A17 17 0 0 1 3 4a1 1 0 0 1 1-1h3.5a1 1 0 0 1 1 1c0 1.25.2 2.45.57 3.57a1 1 0 0 1-.25 1z"/></svg>
      <span>+32471936208</span>
    </li>
    <li class="contacts__item">
      <svg class="contacts__icon" viewBox="0 0 24 24" aria-hidden="true"><path d="M2 5h20v14H2z M4 7v.5l8 5 8-5V7l-8 5z" fill-rule="evenodd"/></svg>
      <span>info@velowerkplaats-martens.be</span>
    </li>
    <li class="contacts__item">
      <svg class="contacts__icon" viewBox="0 0 24 24" aria-hidden="true"><circle cx="12" cy="12" r="10"/></svg>
      <span>www.velowerkplaats-martens.be</span>
    </li>
  </ul>

  <address class="address">
    Molenweg 57<br>
    9470 Oostmolenbeek
  </address>
</section>

</body>
</html>
```